Accommodation in an Executive Apartment for rent could be a Bed and breakfast,

Currently have a website and like the overall look but it needs revamping and want to add an instant booking button, which I would do later as the unit has a channel manager. Also want to be able to post blogs, etc. Need it to be viewed well on smart phones/tablets. all information related to this unit is on the current site which is www.stayfernhollowsuites.com.au if you would view websites similar to roomvista.com and tripnestly.com Must be able to be coded in Wordpress

The current design is done in Wordpress so would want this functionality in any new design.

Target Market(s)

Workers at Parliamentary triangle, Canberra. Workers at Marlowe centre Deakin, Workers at Bellbrook Ashford Hospital, Workers at Tindale Hospital, Public Servants Woden, Workers in Deakin ACT

Industry/Entity Type

Accommodation

Number of Pages Required

5+ page

Font styles to use
Sans Serif

Colors
ec1f27

Requirements
Must have
• Must have a classy look about it. Less clicks through the better. Not to wordy. Hard hitting points,
Nice to have
• Would like to retain the same colour theme and look
Should not have
• anything tacky

```html
<!DOCTYPE html>
<html lang="en">
<head>
<meta charset="utf-8">
<title>Fernhollow Executive Bed and Breakfast</title>
<link rel="stylesheet" href="https://fonts.googleapis.com/css2?family=Open+Sans:wdth,wght@75..100,300..800&display=swap">
<style>
:root{
  --red:#ec1f27;
  --red-dark:#c8161d;
  --ink:#222222;
  --text:#555555;
  --muted:#888888;
  --grey-band:#e6e6e6;
  --panel:#2b2b2b;
  --footer:#3a3a3a;
  --footer-base:#2a2a2a;
  --white:#ffffff;
}
*{margin:0;padding:0;box-sizing:border-box}
html,body{width:1200px;height:3468px;overflow:hidden}
body{position:relative;font-family:"Open Sans",Arial,sans-serif;color:var(--text);background:var(--white)}
.abs{position:absolute}
.cond{font-stretch:75%;font-weight:700}

/* top bar */
.topbar{left:0;top:0;width:1200px;height:37px;background:var(--red);color:#fff;font-size:12px}
.topbar .call{left:104px;top:11px;display:flex;align-items:center;gap:8px}
.topbar .links{left:670px;top:11px;display:flex;gap:26px}
.topbar .select{top:6px;height:24px;border:1px solid rgba(255,255,255,.7);border-radius:2px;font-size:11px;padding:4px 6px}

/* header */
.brand{left:62px;top:82px;font-size:34px;font-weight:700;color:var(--red);letter-spacing:-.5px;font-stretch:75%}
.search{left:900px;top:90px;width:190px;height:46px;border:1px solid #eee;background:#fff;font-size:12px;color:#bbb;padding:14px 12px}
.search svg{position:absolute;right:12px;top:13px}

/* nav */
.nav{left:0;top:190px;width:1200px;height:55px;background:linear-gradient(#f4f4f4,#d9d9d9)}
.nav ul{list-style:none;display:flex;position:absolute;left:128px;top:8px}
.nav li{font-size:13px;font-weight:600;color:var(--red);height:47px;padding:14px 22px;margin-right:14px}
.nav li.active{background:#fff;border-radius:2px 2px 0 0}

/* hero */
.hero{left:0;top:245px;width:1200px;height:587px;background:linear-gradient(180deg,#e8a56a 0%,#b9845c 28%,#5f4a3a 55%,#3b2d24 100%)}
.hero h1{position:absolute;left:0;width:1200px;top:208px;text-align:center;color:#fff;font-size:46px;font-stretch:75%;font-weight:700;text-shadow:0 2px 4px rgba(0,0,0,.4)}
.hero p{position:absolute;left:0;width:1200px;top:272px;text-align:center;color:#fff;font-size:17px}
.btn-red{background:var(--red);color:#fff;font-weight:700;text-align:center;border-radius:2px}
.hero .book{position:absolute;left:536px;top:320px;width:128px;height:52px;line-height:52px;font-size:18px;font-stretch:75%}
.hero .arrow{position:absolute;top:258px;width:62px;height:62px;border-radius:50%;border:2px solid rgba(255,255,255,.35)}

/* intro */
.intro{left:0;top:832px;width:1200px;height:521px;background:var(--grey-band)}
.section-title{font-size:30px;color:var(--ink);font-stretch:75%;font-weight:700}
.intro h2{position:absolute;left:0;width:1200px;top:68px;text-align:center}
.intro p{position:absolute;left:150px;width:900px;top:118px;text-align:center;font-size:12px;line-height:25px;color:#444}
.photo{position:absolute}
.ribbon{position:absolute;left:0;top:0;width:170px;height:170px;overflow:hidden}
.ribbon span{position:absolute;left:-52px;top:48px;width:240px;transform:rotate(-45deg);background:#fff;color:var(--red);text-align:center;font-weight:800;font-size:24px;padding:4px 0;font-stretch:75%}

/* just booked */
.jb-title{left:127px;top:1427px}
.jb-lead{left:127px;top:1480px;width:470px;font-size:12px;line-height:23px;color:#444}
.booking-item h3{position:absolute;font-size:16px;color:var(--ink);font-weight:600}
.booking-item p{position:absolute;font-size:12px;line-height:23px;color:#444;width:220px}
.tag{position:absolute;height:32px;line-height:32px;font-size:10px;font-weight:700;text-align:center;background:#eeeeee}
.tag.red{color:var(--red);width:80px}
.tag.grey{color:#333;width:86px}

.deals{left:659px;top:1433px;width:414px;height:500px;background:var(--panel);color:#fff;box-shadow:0 14px 22px -12px rgba(0,0,0,.45)}
.deals h3{position:absolute;left:0;width:414px;top:22px;text-align:center;font-size:24px;font-stretch:75%;font-weight:700}
.deals .sub{position:absolute;left:0;width:414px;top:64px;text-align:center;font-size:11px;color:#ddd}
.deals label{position:absolute;left:40px;font-size:12px;color:#eee}
.deals .field{position:absolute;left:40px;width:334px;height:33px;background:#fff;border-radius:2px;font-size:11px;color:#aaa;padding:9px 10px}
.deals .field svg{position:absolute;right:9px;top:10px}
.deals .travel{position:absolute;left:40px;top:338px;width:334px;height:30px;background:#5a5a5a;border-radius:2px;font-size:11px;padding:7px 10px;display:flex;gap:12px;align-items:center}
.deals .travel .lbl{color:var(--red)}
.deals .drop{position:absolute;top:380px;height:34px;border:1px solid #777;border-radius:2px;font-size:11px;padding:9px 8px;color:#ddd}
.deals .go{position:absolute;left:155px;top:442px;width:104px;height:36px;line-height:36px;font-size:13px}

/* gallery */
.gallery{left:0;top:2022px;width:1200px;height:413px;background:linear-gradient(180deg,#9aa4ab 0%,#b8bdbf 45%,#8d8f8b 100%)}
.gallery h2{position:absolute;left:0;width:1200px;top:26px;text-align:center;color:#fff}
.frame{position:absolute;top:89px;height:286px;border:7px solid #fff;background:#c9b48f}

/* blog */
.blog-title{left:99px;top:2500px}
.blog-card{left:99px;top:2578px;width:999px;height:363px;border:1px solid #e2e2e2;background:#fff}
.blog-card h3{position:absolute;left:542px;top:12px;font-size:18px;color:var(--red);font-weight:600}
.blog-card h4{position:absolute;left:542px;top:60px;font-size:18px;color:#999;font-weight:400}
.blog-card .text{position:absolute;left:542px;width:420px;font-size:12px;line-height:22px;color:#555}
.price-badge{position:absolute;left:38px;top:320px;width:66px;height:66px;border-radius:50%;background:var(--red);border:3px solid #fff;color:#fff;text-align:center;font-weight:700;font-size:17px;padding-top:14px;line-height:16px}
.price-badge small{display:block;font-size:9px;font-weight:400}

/* newsletter */
.newsletter{left:0;top:3050px;width:1200px;height:102px;background:var(--red);color:#fff}
.newsletter .head{position:absolute;left:242px;top:28px;font-size:16px;font-weight:600}
.newsletter .sub{position:absolute;left:242px;top:52px;font-size:16px}
.newsletter .input{position:absolute;left:623px;top:30px;width:325px;height:42px;background:#fff;color:#555;font-size:12px;padding:13px 12px}
.newsletter .submit{position:absolute;left:948px;top:30px;width:127px;height:42px;line-height:42px;text-align:center;background:#555;font-size:14px}

/* footer */
.footer{left:0;top:3152px;width:1200px;height:253px;background:var(--footer);color:#eee}
.footer h5{position:absolute;top:34px;font-size:15px;font-weight:400}
.footer ul{position:absolute;top:78px;list-style:none;font-size:11px;line-height:29px}
.footer li{display:flex;align-items:center;gap:12px}
.footer li::before{content:"";width:8px;height:8px;border:2px solid #ccc;border-radius:50%}
.footer .about{position:absolute;left:99px;top:78px;font-size:11px;line-height:26px;width:170px}
.footer .partner{position:absolute;top:150px;font-size:26px;font-weight:800;color:#fff}
.footer .contact{position:absolute;left:926px;font-size:12px;line-height:22px}
.base{left:0;top:3405px;width:1200px;height:63px;background:var(--footer-base);color:#ddd;font-size:12px}
.base .copy{position:absolute;left:99px;top:24px}
.base .legal{position:absolute;left:730px;top:24px;display:flex;gap:10px}
</style>
</head>
<body>

<!-- top bar -->
<div class="abs topbar">
  <div class="abs call">
    <svg width="13" height="13" viewBox="0 0 24 24"><path fill="#fff" d="M6.6 10.8a15 15 0 0 0 6.6 6.6l2.2-2.2a1 1 0 0 1 1-.25 11.4 11.4 0 0 0 3.6.57 1 1 0 0 1 1 1V20a1 1 0 0 1-1 1A17 17 0 0 1 3 4a1 1 0 0 1 1-1h3.5a1 1 0 0 1 1 1c0 1.25.2 2.46.57 3.6a1 1 0 0 1-.25 1z"/></svg>
    <span>Call Us Now : 0255501842</span>
  </div>
  <div class="abs links"><span>My Account</span><span>Wish List</span><span>Login</span><span>Sign Up</span></div>
  <div class="abs select" style="left:982px;width:46px">EN ▾</div>
  <div class="abs select" style="left:1052px;width:46px">$ ▾</div>
</div>

<!-- header -->
<div class="abs brand">Fernhollow executive bed and breakfast</div>
<div class="abs search">Search
  <svg width="18" height="18" viewBox="0 0 24 24"><circle cx="10" cy="10" r="6.5" fill="none" stroke="#ec1f27" stroke-width="3"/><path d="M15 15l6 6" stroke="#ec1f27" stroke-width="3" stroke-linecap="round"/></svg>
</div>

<!-- navigation -->
<nav class="abs nav">
  <ul>
    <li class="active">Home</li><li>B&amp;B Accommodation</li><li>Gallery</li><li>What's Nearby</li><li>Guest Book</li><li>Useful Links</li><li>Contact Us</li>
  </ul>
</nav>

<!-- hero -->
<section class="abs hero" role="img" aria-label="Poolside wooden deck loungers at sunset overlooking the sea">
  <div class="arrow" style="left:18px"></div>
  <div class="arrow" style="left:1120px"></div>
  <h1>Feel the Ocean Breeze</h1>
  <p>Rooms from $199/night!</p>
  <div class="btn-red book">BOOK NOW</div>
</section>

<!-- intro -->
<section class="abs intro">
  <h2 class="section-title">A PERFECT, SMALL HOTEL</h2>
  <p>Lorem Ipsum is simply dummy text of the printing and typesetting industry. Lorem Ipsum has been the industry's standard dummy text ever since the 1500s, when an unknown printer took a galley of type and scrambled it to make a type specimen book. I</p>
  <div class="photo" style="left:99px;top:190px;width:319px;height:252px;background:linear-gradient(180deg,#6e7fa3 0%,#e9a45a 55%,#c8763a 100%)" role="img" aria-label="Waterfront square with a column at sunset">
    <div class="ribbon"><span>40 % OFF</span></div>
  </div>
  <div class="photo" style="left:439px;top:190px;width:319px;height:252px;background:linear-gradient(180deg,#7b8a97 0%,#c7a27a 50%,#2d2a28 100%)" role="img" aria-label="Palm tree silhouette by the sea at sunset"></div>
  <div class="photo" style="left:781px;top:190px;width:319px;height:252px;background:linear-gradient(180deg,#4f86c6 0%,#d49a6a 50%,#3b5f83 100%)" role="img" aria-label="Colourful seaside village houses reflected in a harbour"></div>
</section>

<!-- just booked -->
<h2 class="abs section-title jb-title">JUST BOOKED</h2>
<p class="abs jb-lead">Lorem Ipsum is simply dummy text of the printing and typesetting industry. Lorem Ipsum has been the industry's standard dummy text ever since the 1500s.</p>

<div class="booking-item">
  <div class="photo" style="left:125px;top:1551px;width:226px;height:155px;background:linear-gradient(180deg,#e9d3c0,#a8503c 60%,#5a2a22)" role="img" aria-label="Hotel restaurant interior with red chairs"></div>
  <h3 style="left:386px;top:1548px">Someone from India</h3>
  <p style="left:386px;top:1580px">Lorem Ipsum is simply dummy text of the printing and typesetting industry. Lorem Ipsum has been the industry's standard ...</p>
  <div class="tag red" style="left:386px;top:1676px">JUST BOOKED</div>
  <div class="tag grey" style="left:504px;top:1676px">DETAILS</div>
</div>
<div class="booking-item">
  <div class="photo" style="left:125px;top:1759px;width:226px;height:153px;background:linear-gradient(180deg,#cfe3f0,#5e7e5a 45%,#3fb3c8 75%,#2a8fa6)" role="img" aria-label="Resort pool with thatched umbrellas"></div>
  <h3 style="left:386px;top:1754px">Someone from Usa</h3>
  <p style="left:386px;top:1786px">Lorem Ipsum is simply dummy text of the printing and typesetting industry. Lorem Ipsum has been the industry's standard ...</p>
  <div class="tag red" style="left:386px;top:1882px">JUST BOOKED</div>
  <div class="tag grey" style="left:504px;top:1882px">DETAILS</div>
</div>

<div class="abs deals">
  <h3><svg width="22" height="22" viewBox="0 0 24 24" style="vertical-align:-3px;margin-right:8px"><circle cx="10" cy="10" r="6.5" fill="none" stroke="#fff" stroke-width="3"/><path d="M15 15l6 6" stroke="#fff" stroke-width="3" stroke-linecap="round"/></svg>FIND THE BEST DEALS</h3>
  <div class="sub">20 million rooms are at your fingertips</div>
  <label style="top:100px">Destination/Hotel Name</label>
  <div class="field" style="top:128px">eg - country, city , district or landmark</div>
  <label style="top:178px">Check-in Date</label>
  <div class="field" style="top:203px"><svg width="12" height="12" viewBox="0 0 12 12"><rect x="1" y="2" width="10" height="9" fill="none" stroke="#ec1f27" stroke-width="1.5"/><path d="M1 5h10" stroke="#ec1f27" stroke-width="1.5"/></svg></div>
  <label style="top:254px">Check-Out Date</label>
  <div class="field" style="top:270px"><svg width="12" height="12" viewBox="0 0 12 12"><rect x="1" y="2" width="10" height="9" fill="none" stroke="#ec1f27" stroke-width="1.5"/><path d="M1 5h10" stroke="#ec1f27" stroke-width="1.5"/></svg></div>
  <div class="travel"><span class="lbl">Traveling for</span><span>☑ Work</span><span>■ Leisure</span></div>
  <div class="drop" style="left:69px;width:66px">Room ▾</div>
  <div class="drop" style="left:159px;width:72px">Adults ▾</div>
  <div class="drop" style="left:262px;width:70px">Childs ▾</div>
  <div class="btn-red go">Search</div>
</div>

<!-- gallery -->
<section class="abs gallery" role="img" aria-label="Faded beach backdrop with a woman in a sun hat">
  <h2 class="section-title">GALLERY</h2>
  <div class="frame" style="left:102px;width:319px;background:linear-gradient(180deg,#e8dcc8,#9a7a5a 60%,#4a2e22)" role="img" aria-label="Dining table set with wine and red napkins"></div>
  <div class="frame" style="left:439px;width:315px;background:linear-gradient(180deg,#e6d6b0,#b08a5c 55%,#6a4a30)" role="img" aria-label="Living room with sofas and a coffee table"></div>
  <div class="frame" style="left:781px;width:319px;background:linear-gradient(180deg,#efe2c2,#c8a87a 55%,#8a6540)" role="img" aria-label="Open-plan lounge with television and dining table"></div>
</section>

<!-- blog -->
<h2 class="abs section-title blog-title">LATEST BLOG</h2>
<article class="abs blog-card">
  <div class="photo" style="left:0;top:0;width:500px;height:363px;background:linear-gradient(180deg,#cfd6d8,#9aa6a8 45%,#e8e4df 70%,#6a5a50)" role="img" aria-label="Bright bedroom with a large bed and sea view windows"></div>
  <svg class="abs" style="left:418px;top:10px" width="50" height="44" viewBox="0 0 24 22"><path fill="#555" d="M12 21l-1.5-1.3C5 15 2 12.2 2 8.5 2 5.4 4.4 3 7.5 3c1.7 0 3.4.8 4.5 2.1C13.1 3.8 14.8 3 16.5 3 19.6 3 22 5.4 22 8.5c0 3.7-3 6.5-8.5 11.2z"/></svg>
  <div class="abs" style="left:0;top:336px;width:500px;height:27px;background:rgba(0,0,0,.45);color:#fff;font-size:11px;padding:6px 120px">Gardenia Main Room</div>
  <div class="price-badge">109$<small>per night</small></div>
  <h3>Gardenia Main Room</h3>
  <h4>Sed ut perspiciatis unde</h4>
  <div class="abs" style="left:542px;top:104px;display:flex;gap:3px">
    <svg width="72" height="14" viewBox="0 0 90 16"><g fill="#f2b01e"><path id="st" d="M8 1l2.1 4.6 5 .5-3.8 3.3 1.1 4.9L8 11.8 3.6 14.3l1.1-4.9L.9 6.1l5-.5z"/><use href="#st" x="18"/><use href="#st" x="36"/><use href="#st" x="54"/></g><path d="M80 1l2.1 4.6 5 .5-3.8 3.3 1.1 4.9L80 11.8z" fill="#f2b01e"/><path d="M80 1l-2.1 4.6-5 .5 3.8 3.3-1.1 4.9L80 11.8z" fill="#ccc"/></svg>
  </div>
  <div class="abs" style="left:652px;top:102px;font-size:12px">60 reviews</div>
  <svg class="abs" style="left:740px;top:100px" width="18" height="16" viewBox="0 0 18 16"><path d="M2 2h11v8H7l-3 3v-3H2z" fill="none" stroke="#777" stroke-width="1.3"/></svg>
  <div class="abs" style="left:768px;top:102px;font-size:12px">Comments</div>
  <p class="text" style="top:128px">Sed ut perspiciatis unde omnis iste natus error sit voluptatem accusantium doloremque laudantium, totam rem aperiam, eaque ipsa quae ab.Sed ut perspiciatis unde omnis iste natus error sit voluptatem accusantium.</p>
  <p class="text" style="top:220px">Sed ut perspiciatis unde omnis iste natus error sit voluptatem accusantium doloremque laudantium, totam rem aperiam, eaque ipsa quae ab.Sed ut perspiciatis unde omnis iste natus error sit voluptatem accusantium.</p>
  <div class="abs btn-red" style="left:543px;top:284px;width:126px;height:52px;line-height:52px;font-size:17px;font-stretch:75%">view more</div>
</article>

<!-- newsletter -->
<section class="abs newsletter">
  <svg class="abs" style="left:118px;top:22px" width="86" height="62" viewBox="0 0 86 62"><g fill="none" stroke="rgba(255,255,255,.25)" stroke-width="3"><rect x="4" y="4" width="78" height="54"/><path d="M4 4l39 30 39-30"/></g></svg>
  <div class="head">JOIN OUR NEWSLETTER</div>
  <div class="sub">Lorem ipsum dolor sit amet, consectetur</div>
  <div class="input">Enter your E - mail</div>
  <div class="submit">SUBSCRIBE</div>
</section>

<!-- footer -->
<footer class="abs footer">
  <h5 style="left:99px">About Our Company</h5>
  <p class="about">Lorem ipsum dolor sit amet, consectetur adipiscing elit.</p>
  <div class="partner" style="left:99px">AirLink</div>
  <div class="partner" style="left:204px">StreamBox</div>

  <h5 style="left:414px">QUICK LINK</h5>
  <ul style="left:414px"><li>B&amp;B Accommodation</li><li>Gallery</li><li>What's Nearby</li><li>Guest Book</li><li>Useful Links</li></ul>

  <h5 style="left:667px">INFORMATION</h5>
  <ul style="left:667px"><li>placeat facere</li><li>Sri Lanka Events</li><li>Travel and Health</li><li>Payment Centre</li><li>Finibus Bonorum</li></ul>

  <h5 style="left:926px">CONTACT US</h5>
  <div class="contact" style="top:72px">Larkvale PO Box 2281,<br>Ashmere NSW 2090</div>
  <svg class="abs" style="left:926px;top:130px" width="16" height="16" viewBox="0 0 24 24"><path fill="none" stroke="#ccc" stroke-width="2" d="M6.6 10.8a15 15 0 0 0 6.6 6.6l2.2-2.2 4.6 1.3V20A17 17 0 0 1 4 4h3.5l1.3 4.6z"/></svg>
  <div class="contact" style="left:956px;top:127px">+61 0400 555 218</div>
  <svg class="abs" style="left:926px;top:162px" width="18" height="14" viewBox="0 0 18 14"><rect x="1" y="1" width="16" height="12" fill="none" stroke="#ccc" stroke-width="1.5"/><path d="M1 1l8 6 8-6" fill="none" stroke="#ccc" stroke-width="1.5"/></svg>
  <div class="contact" style="left:956px;top:158px">info@ fernhollowstay.com</div>
</footer>

<div class="abs base">
  <div class="copy">Copyright © 2015 fernhollowsuites.com. All Rights Reserved.</div>
  <div class="legal"><span>Terms &amp; Conditions</span><span>/</span><span>Privacy &amp; Disclaimer</span><span>/</span><span>Returns &amp; Refunds</span><span style="margin-left:16px">C 24</span></div>
</div>

</body>
</html>
```